依頼詳細
ニュースレターのリニューアルに伴う「ニュースレターのテンプレート」作成をお願いします。
下記の「最終成果物」と「必須掲載項目」を満たしていれば、デザインやレイアウトは問いません。お任せいたします。

【最終成果物】
納品は「InDesign」ファイルでお願いします。

サイズ:A4 中綴じ(左開き)横書き

希望する納品物は次の2点です。
1.表紙
2.見開き2ページ(表紙のあとのP2~P3)

下記、必須掲載項目のうち、2~9は納品後テキストや画像の変更を想定しています。
編集可能な状態で作成してください。

【必須掲載項目】
以下は「表紙」と「見開き2ページ」で必ず入れていただきたい項目と挿入するテキストになります。
各項目のデザイン、レイアウト(ページ数以外)はお任せいたします。

必須掲載項目は添付ファイル「必須掲載項目.pdf」にもまとめてあります。ご参照ください。

≪ 表紙 ≫
1. タイトル
挿入テキスト:Harbor insight Bulletin

2. サブタイトル
挿入テキスト:港から届ける、経営の実践レポート。”キーワードをせいするもの、ネットを制す”

3. 号数
挿入テキスト:150号

4. 発行年月
挿入テキスト:2022年12月

5. 特集見出し
挿入テキスト:特集
※ サンプルでハイライトに該当する部分になります。
※ 見出しは2件掲載する予定です。テキストの分量はサンプルと同程度を想定してください。

6. 巻頭言タイトル
挿入テキスト:巻頭言

7. 筆者顔写真
挿入画像:ファイル「筆者写真.png」

8. ページ数(フッター)
挿入テキスト:該当ページ数 Harbor insight 号数(例:1 Harbor insight 150号)
※ レイアウトは左寄せにしてください。

≪見開き2ページ≫
9. ページ数(フッター)
挿入テキスト:該当ページ数 Harbor insight 号数(例:2 Harbor insight 150号)
※ 表紙のフッターからの連番になります。
※ 2ページ(右側ページ)は右寄せ、3ページ(左側ページ)は左寄せにレイアウトしてください。
記載項目
・色はコーポレートカラーの HI DEEP BLUE(RGB:R:0 G:0 B:192、#0000c0)をベースにHI RED PURPLE(RGB: R:230 G:0 B:255、#e600ff)を使用してください。
※ コーポレートカラーの詳細は添付ファイル「必須掲載項目.pdf」をご参照ください。

イメージ、配色などは弊社HPをご参照ください。
https://www.hbi-example.co.jp/

参考として弊社ロゴデータを添付いたします。ご参照ください(ファイル名:harborinsight_logo.zip)

・ニュースレターはデータと印刷両方で配布いたします。カラーで作成していただきたいですが、印刷時はモノクロになることを考慮したデザインにしていただければと思います。

・フォントは有料フォントは使用せず、Adobeでダウンロード可能なものをご使用ください。

・サンプルとして現在仕様しているテンプレートで作成したニュースレターを添付いたします。(ファイル名:Sample.pdf)
希望イメージ
シンプル 複雑
単色 カラフル
暗い 明るい
日常 高級
遊び心 厳粛
未来的 伝統的
女性的 男性的
希望する色
コーポレートカラーをベースに。カラーコードは添付を参照下さい
補足説明
最終納品はInDesign形式でお願いします。
依頼詳細の【必須掲載項目】のうち、8と9の記載内容に誤りがありましたので、
訂正させていただきます。大変失礼いたしました。

誤)
8. ページ数(フッター)
※ レイアウトは左寄せにしてください。

正)
8. ページ数(フッター)
※ レイアウトは右寄せにしてください。

誤)
9. ページ数(フッター)
※ 表紙のフッターからの連番になります。

正)
9. ページ数(フッター)
※ 表紙のフッターからの連番になります。
※ 2ページ(左側ページ)は左寄せ、3ページ(右側側ページ)は右寄せにレイアウトしてください。

(※ 添付の指示書も誤った内容となっています。お手数ですがこちらの訂正をご参照ください。)

既にご提案いただいている方のうち、当初の指示に従って作成していただいている方については、
再提案いただく必要はございません。
採用となった場合、修正の相談をさせていただければと思います。
■ 選んだ理由

コンセプトとこちらの希望をよくご理解いただき、イメージ通りのデザインだったため選ばせていただきました。

■ 提案者全員のお礼・コメント

このたびはご提案いただきありがとうございました。

皆さん弊社のHPを読み込んでくださったり、
コンセプト実現のためのアイデアをご提案いただいたり、
よいご提案ばかりで選ぶのにお時間をいただいてしまいました。

またデザイン関連で必要が生じたときはワークモールで公募したいと思います。
その際はぜひご応募いただければ幸いです。

```html
<!DOCTYPE html>
<html lang="ja">
<head>
<meta charset="utf-8">
<title>Harbor insight Bulletin Vol.150</title>
<link href="https://fonts.googleapis.com/css2?family=Noto+Sans+JP:wght@400;500;700;900&display=swap" rel="stylesheet">
<style>
  :root {
    --deep-blue: #0000c0;
    --navy: #06105e;
    --mid-blue: #1c3fc8;
    --sky: #58b4f0;
    --red-purple: #e600ff;
    --accent-magenta: #d4007a;
    --ink: #222;
    --grey-text: #8a8a8a;
    --paper: #ffffff;
    --tagline-yellow: #ffe88a;
  }
  * { box-sizing: border-box; margin: 0; padding: 0; }
  html, body { width: 849px; height: 1200px; overflow: hidden; background: var(--paper); }
  body { font-family: "Noto Sans JP", sans-serif; color: var(--ink); position: relative; }

  .masthead {
    position: absolute; left: 0; top: 0; width: 849px; height: 200px;
    background: linear-gradient(100deg, var(--navy) 0%, var(--deep-blue) 55%, var(--mid-blue) 100%);
    overflow: hidden;
  }
  .masthead svg.stripes { position: absolute; inset: 0; }
  .masthead-rule { position: absolute; left: 0; top: 196px; width: 849px; height: 4px; background: var(--sky); }
  .lead-line { position: absolute; left: 36px; top: 26px; color: #cfe0ff; font-size: 17px; font-weight: 500; letter-spacing: 0.02em; }
  .tagline { position: absolute; left: 36px; top: 54px; color: var(--tagline-yellow); font-size: 29px; font-weight: 900; letter-spacing: 0.02em; font-style: italic; }
  .title { position: absolute; left: 34px; top: 104px; color: #fff; font-size: 52px; font-weight: 500; letter-spacing: 0.005em; }

  .issue-badge {
    position: absolute; right: 30px; top: 22px; width: 134px; height: 72px;
    background: #fff; color: var(--deep-blue); text-align: center; padding-top: 6px;
  }
  .issue-badge .vol { font-size: 28px; font-weight: 700; line-height: 1.1; }
  .issue-badge .date { font-size: 19px; font-weight: 500; line-height: 1.3; }

  .feature { position: absolute; left: 36px; top: 216px; width: 780px; }
  .feature-tag {
    position: absolute; left: 0; top: 0; width: 68px; height: 124px;
    background: var(--accent-magenta); color: #fff; font-weight: 900; font-size: 40px;
    display: flex; flex-direction: column; align-items: center; justify-content: center; line-height: 1.1;
  }
  .feature-list { list-style: none; position: absolute; left: 86px; top: 4px; width: 690px; }
  .feature-list li {
    font-size: 19px; font-weight: 700; line-height: 1.35; color: #333; word-break: break-all;
    padding-bottom: 6px; margin-bottom: 8px; border-bottom: 1px solid #cfcfcf;
  }

  .section-bar {
    position: absolute; left: 36px; top: 362px; width: 777px; height: 26px;
    background: #1a1a1a; border-radius: 13px; color: #fff;
    font-size: 15px; font-weight: 700; text-align: center; line-height: 26px; letter-spacing: 0.6em;
  }

  .foreword { position: absolute; left: 40px; top: 414px; width: 772px; height: 698px; overflow: hidden; }
  .author-photo {
    float: left; width: 126px; height: 160px; margin: 2px 22px 8px 0;
    background: linear-gradient(160deg, #9fb3c4 0%, #5d6f7f 60%, #3a4450 100%);
  }
  .foreword p {
    font-size: 12.4px; line-height: 19.4px; color: var(--grey-text);
    word-break: break-all; text-indent: 1em; letter-spacing: 0.02em;
  }

  .footer { position: absolute; left: 0; top: 1143px; width: 849px; height: 22px; }
  .footer-band {
    position: absolute; left: 0; top: 0; width: 772px; height: 22px;
    background: linear-gradient(90deg, #ffffff 0%, #a9c6f4 35%, var(--mid-blue) 100%);
  }
  .footer-label { position: absolute; right: 92px; top: 2px; color: #fff; font-size: 13px; font-weight: 500; }
  .page-number {
    position: absolute; left: 776px; top: 0; width: 48px; height: 22px;
    background: var(--accent-magenta); color: #fff; font-size: 13px; text-align: center; line-height: 22px;
  }
</style>
</head>
<body>
  <header class="masthead">
    <svg class="stripes" width="849" height="200" viewBox="0 0 849 200" aria-hidden="true">
      <polygon points="470,0 560,0 420,200 330,200" fill="#ffffff" opacity="0.06"/>
      <polygon points="590,0 640,0 500,200 450,200" fill="#ffffff" opacity="0.08"/>
      <polygon points="670,0 760,0 620,200 530,200" fill="#6fa8ff" opacity="0.12"/>
      <polygon points="780,0 849,0 849,60 720,200 650,200" fill="#ffffff" opacity="0.07"/>
      <polygon points="560,200 849,90 849,200" fill="#0a2bb0" opacity="0.5"/>
    </svg>
    <p class="lead-line">港から届ける、経営の実践レポート。</p>
    <p class="tagline">“潮目を読むもの、市場を制す”</p>
    <h1 class="title">Harbor insight Bulletin</h1>
    <div class="issue-badge">
      <div class="vol">Vol.150</div>
      <div class="date">2022.12.00</div>
    </div>
    <div class="masthead-rule"></div>
  </header>

  <section class="feature">
    <div class="feature-tag"><span>特</span><span>集</span></div>
    <ul class="feature-list">
      <li>●○○○○○○○○○○○○○○○○○○○○○○○○○○○○○○○○○○○○○○○○○○○○○○○○○</li>
      <li>●○○○○○○○○○○○○○○○○○○○○○○○○○○○○○○○○○○○○○○○○○○○○○○○○</li>
    </ul>
  </section>

  <h2 class="section-bar">巻頭言</h2>

  <article class="foreword">
    <div class="author-photo" role="img" aria-label="筆者の顔写真"></div>
    <p>○○○○○○○○○○○○○○○○○○○○○○○○○○○○○○○○○○○○○○○○○○○○○○○○○○○○○○○○○○○○○○○○○○○○○○○○○○○○○○○○○○○○○○○○○○○○○○○○○○○○○○○○○○○○○○○○○○○○○○○○○○○○○○○○○○○○○○○○○○○○○○○○○○○○○○○○○○○○○○○○○○○○○○○○○○○○○○○○○○○○○○○○○○○○○○○○○○○○○○○○○○○○○○○○○○○○○○○○○○○○○○○○○○○○○○○○○○○○○○○○○○○○○○○○○○○○○○○○○○○○○○○○○○○○○○○○○○○○○○○○○○○○○○○○○○○○○○○○○○</p>
    <p>○○○○○○○○○○○○○○○○○○○○○○○○○○○○○○○○○○○○○○○○○○○○○○○○○○○○○○○○○○○○○○○○○○○○○○○○○○○○○○○○○○○○○○○○○○○○○○○○○○○○○○○○○○○○○○○○○○○○○○○○○○○○○○○○○○○○○○○○○○○○○○○○○○○○○○○○○○○○○○○○○○○○○○○○○○○○○○○○○○○○○○○○○○○○○○○○○○○○○○○○○○○○○○○○○○○○○○○○○○○○○○○○○○○○○○○○○○○○○○○○○○○○○○○○○○</p>
    <p>○○○○○○○○○○○○○○○○○○○○○○○○○○○○○○○○○○○○○○○○○○○○○○○○○○○○○○○○○○○○○○○○○○○○○○○○○○○○○○○○○○○○○○○○○○○○○○○○○○○○○○○○○○○○○○○○○○○○○○○○○○○○○○○○○○○○○○○○○○○○○○○○○○○○○○○○○○○○○○○○○○○○○○○○○○○○○○○○○○○○○○○○○○○○○○○○○○○○○○○○○○○○○○○○○○○○○○○○○○○○○○○○○○</p>
    <p>○○○○○○○○○○○○○○○○○○○○○○○○○○○○○○○○○○○○○○○○○○○○○○○○○○○○○○○○○○○○○○○○○○○○○○○○○○○○○○○○○○○○○○○○○○○○○○○○○○○○○○○○○○○○○○○○○○○○○○○○○○○○○○○○○○○○○○○○○○○○○○○○○○○○○○○○○○○○○○○○○○○○○○○○○○○○○○○○○○○○○○○○○○○○○○○○○○○○○○○○○○○○○○○○○○○○○○○○○○○○○○○○○○○○○○○○○○○○○○○○○○○○○○○○○○○○○○○○○○○○○○○○○○○○○○○○○○○○○○○○○○○○○○○○○○○○○○○○○○○</p>
    <p>○○○○○○○○○○○○○○○○○○○○○○○○○○○○○○○○○○○○○○○○○○○○○○○○○○○○○○○○○○○○○○○○○○○○○○○○○○○○○○○○○○○○○○○○○○○○○○○○○○○○○○○○○○○○○○○○○○○○○○○○○○○○○○○○○○○○○○○○○○○○○○○○○○○○○○○○○○○○○○○○○○○○○○○○○○○○○○○○○○○○○○○○○○○○○○○○○○○○○○○○○○○○○○○○○○○○○○○○○○○○○○○○○○○○○○○○○○○○○○○○○○○○○○○○○○○○○○</p>
    <p>○○○○○○○○○○○○○○○○○○○○○○○○○○○○○○○○○○○○○○○○○○○○○○○○○○○○○○○○○○○○○○○○○○○○○○○○○○○○○○○○○○○○○○○○○○○○○○○○○○○○○○○○○○○○○○○○○○○○○○○○○○○○○○○○○○○○○○○○○○○○○○○○○○○○○○○○○○○○○○○○○○○○○○○○○○○○○○○○○○○○○○○○○○○○○○○○○○○○○○○○○○○○○○○○○○○○○○○○○○○○○○○○○○○○○○○○○○○○○○○○○○○○○○○○○○○○○○○○○○○○○○○○○○○○○○○○○○○○○○○○○○○○○○○○○○○○○○○○</p>
    <p>○○○○○○○○○○○○○○○○○○○○○○○○○○○○○○○○○○○○○○○○○○○○○○○○○○○○○○○○○○○○○○○○○○○○○○○○○○○○○○○○○○○○○○○○○○○○○○○○○○○○○○○○○○○○○○○○○○○○○○○○○○○○○○○○○○○○○○○○○○○○○○○○○○○○○○○○○○○○○○○○○○○○○○○○○○○○○○○○○○○○○○○○○○○○○○○○○○○○○○○○○○○○○○○○○○○○○○○○○○○○○○○○○○○○○○○○○○○○○○○○○○○○○○○○○○</p>
    <p>○○○○○○○○○○○○○○○○○○○○○○○○○○○○○○○○○○○○○○○○○○○○○○○○○○○○○○○○○○○○○○○○○○○○○○○○○○○○○○○○○○○○○○○○○○○○○○○○○○○○○○○○○○○○○○○○○○○○○○○○○○○○○○○○○○○○○○○○○○○○○○○○○○○○○○○○○○○○○○○○○○○○○○○○○○○○○○○○○○○○○○○○○○○○○○○○○○○○○○○○○○○○○○○○○○○○○○○○○○○○○○○○○○○○○○○○○○○○○○○○○○○○○○○○○○○○○○○○○○○○○○○○○○○○○○○○○</p>
  </article>

  <footer class="footer">
    <div class="footer-band"></div>
    <span class="footer-label">Harbor insight vol.150</span>
    <span class="page-number">1</span>
  </footer>
</body>
</html>
```